"Fern Hollow Realty" is the name of my real estate company

This is for a: "for sale" sign, looking for a minimalist design, wire frame outline of a midcentury modern homes roof line or elevation?

My name is: Derek Malloy (needed)
My Cell # is: 555 204 3967 (needed)
My BRE license # is: 04827265 (needed)
BRE needs to be displayed in this format: BRE 04827265 (needed)
The white outline on the sign riders 'pictured" may work on large sign
Note font on pictured rider sign

This design is for a real estate "for sale" sign or sandwich board sign. Do Not include the words "For Sale" on the sign.

The measurements are 36" inches (91.44 cm) Length, or tall X 24" inches (60.90 cm) Wide.

|
3
---- 24 ----
6
|

Sorry I wasn't more specific earlier. I'd like the elements of the sign to be scaled in size according to their importance, from largest to smallest:

My name: Derek Malloy
My phone number: 555-204-3967
My company name: Fern Hollow Realty
My license number: BRE 04827265 (This can be much smaller than the smallest text)
Additionally, please incorporate contemporary to mid-century modern elements on the wire frame roofline or a simple roof-like design.

Thank you!

Best regards,
Derek

```html
<!DOCTYPE html>
<html lang="en">
<head>
<meta charset="UTF-8">
<title>Fern Hollow Realty – Yard Sign</title>
<link rel="stylesheet" href="https://fonts.googleapis.com/css2?family=Poppins:wght@400;600&display=swap">
<style>
  :root {
    --backdrop: #cccccc;
    --sign-black: #000000;
    --ink-white: #ffffff;
    --frame-line: #e6e6e6;
    --roof-tone-1: #0a0a0a;
    --roof-tone-2: #1c1c1c;
  }
  * { margin: 0; padding: 0; box-sizing: border-box; }
  html, body {
    width: 867px;
    height: 1200px;
    overflow: hidden;
    background: var(--backdrop);
  }
  .sign {
    position: absolute;
    left: 33px;
    top: 0;
    width: 800px;
    height: 1200px;
    background: var(--sign-black);
    color: var(--ink-white);
    font-family: "Poppins", sans-serif;
  }
  .sign__frame {
    position: absolute;
    left: 66px;
    top: 66px;
    width: 668px;
    height: 1068px;
    border: 1.5px solid var(--frame-line);
  }
  .sign__company {
    position: absolute;
    left: 0;
    right: 0;
    top: 262px;
    text-align: center;
    font-weight: 600;
    font-size: 46px;
    line-height: 1;
    letter-spacing: 0.5px;
  }
  .sign__agent {
    position: absolute;
    left: 0;
    right: 0;
    top: 482px;
    text-align: center;
    font-weight: 400;
    font-size: 90px;
    line-height: 1.2;
  }
  .sign__rule {
    position: absolute;
    left: 151px;
    width: 500px;
    height: 2px;
    background: linear-gradient(90deg, rgba(255,255,255,0) 0%, rgba(255,255,255,0.35) 20%, rgba(255,255,255,0.95) 50%, rgba(255,255,255,0.35) 80%, rgba(255,255,255,0) 100%);
  }
  .sign__rule--top { top: 630px; }
  .sign__rule--bottom { top: 732px; }
  .sign__phone {
    position: absolute;
    left: 0;
    right: 0;
    top: 639px;
    text-align: center;
    font-weight: 400;
    font-size: 62px;
    line-height: 1.2;
    letter-spacing: 1px;
  }
  .sign__license {
    position: absolute;
    left: 0;
    right: 0;
    top: 769px;
    text-align: center;
    font-weight: 400;
    font-size: 28px;
    line-height: 1.2;
  }
  .sign__roofline {
    position: absolute;
    left: 121px;
    top: 969px;
    width: 552px;
    height: 154px;
  }
</style>
</head>
<body>
  <div class="sign">
    <div class="sign__frame"></div>
    <div class="sign__company">Fern Hollow Realty</div>
    <div class="sign__agent">Derek Malloy</div>
    <div class="sign__rule sign__rule--top"></div>
    <div class="sign__phone">555-204-3967</div>
    <div class="sign__rule sign__rule--bottom"></div>
    <div class="sign__license">BRE 04827265</div>
    <svg class="sign__roofline" role="img" aria-label="Wireframe outline of a mid-century modern house roofline with chimney" viewBox="0 0 552 154" preserveAspectRatio="none">
      <defs>
        <linearGradient id="roofTone" x1="0" y1="0" x2="0" y2="1">
          <stop offset="0" stop-color="var(--roof-tone-1)"/>
          <stop offset="1" stop-color="var(--roof-tone-2)"/>
        </linearGradient>
      </defs>
      <rect width="552" height="154" fill="url(#roofTone)"/>
    </svg>
  </div>
</body>
</html>
```